Its a flyer to a course entitled :
Ultrasound Course

Basically we teach students about the use of ultrasound for very sick patients

-I need a title in 3D
-I need an attractive design please
something extraordinary

Please if you have any ongoing project let me know Thanks

Dear Designers Was looking for something new that I did not see before, unfortunately did not find that yet! To clarify the idea, remember the T.V series 'KJ'.. so we have a sick patient like the one you have seen in the series and now we are using Ultrasound to help get the diagnosis and even it helps us in the procedures so basically will use the ultrasound to help saving those patients and give them the treatment in a short time.j

```html
<!DOCTYPE html>
<html lang="en">
<head>
<meta charset="utf-8">
<title>Emergency &amp; Critical Care Ultrasound Course</title>
<link rel="stylesheet" href="https://fonts.googleapis.com/css2?family=Montserrat:ital,wght@0,700;0,800;1,800&family=Oswald:wght@400;500;600&display=swap">
<style>
  :root {
    --navy-deep: #050d1c;
    --navy: #0b2245;
    --blue-glow: #2f7fd0;
    --blue-light: #8fc4f2;
    --blue-text: #3d8ad4;
    --blue-bright: #6fb2ef;
    --white: #ffffff;
    --extrude-1: #c9ced6;
    --extrude-2: #9aa1ac;
    --extrude-3: #6d7480;
  }
  html, body {
    margin: 0;
    padding: 0;
    width: 816px;
    height: 1200px;
    overflow: hidden;
    background: var(--navy-deep);
  }
  .flyer {
    display: block;
    width: 816px;
    height: 1200px;
  }
  .presenter { font-family: 'Montserrat', sans-serif; font-weight: 700; fill: var(--white); }
  .presenter .company { font-weight: 800; }
  .event-date { font-family: 'Oswald', sans-serif; font-weight: 500; fill: var(--blue-light); }
  .title-line { font-family: 'Montserrat', sans-serif; font-weight: 800; font-style: italic; }
  .tagline { font-family: 'Oswald', sans-serif; font-weight: 500; fill: var(--blue-text); }
  .tagline .highlight { fill: var(--blue-bright); font-weight: 600; }
  .contact { font-family: 'Oswald', sans-serif; font-weight: 500; fill: var(--white); }
</style>
</head>
<body>
<svg class="flyer" viewBox="0 0 816 1200" xmlns="http://www.w3.org/2000/svg" role="img" aria-label="Emergency and Critical Care Ultrasound Course flyer">
  <defs>
    <radialGradient id="bg-glow" cx="50%" cy="45%" r="70%">
      <stop offset="0" stop-color="#1d4f8c"/>
      <stop offset="0.35" stop-color="var(--navy)"/>
      <stop offset="1" stop-color="var(--navy-deep)"/>
    </radialGradient>
    <radialGradient id="top-sheen" cx="50%" cy="0%" r="60%">
      <stop offset="0" stop-color="#2a5f9c" stop-opacity="0.55"/>
      <stop offset="1" stop-color="#2a5f9c" stop-opacity="0"/>
    </radialGradient>
    <radialGradient id="flare" cx="50%" cy="50%" r="50%">
      <stop offset="0" stop-color="#ffffff" stop-opacity="1"/>
      <stop offset="0.15" stop-color="#9fd0ff" stop-opacity="0.8"/>
      <stop offset="0.5" stop-color="var(--blue-glow)" stop-opacity="0.3"/>
      <stop offset="1" stop-color="var(--blue-glow)" stop-opacity="0"/>
    </radialGradient>
    <linearGradient id="flare-streak" x1="0" x2="1" y1="0" y2="0">
      <stop offset="0" stop-color="#7fc0ff" stop-opacity="0"/>
      <stop offset="0.5" stop-color="#dff0ff" stop-opacity="0.9"/>
      <stop offset="1" stop-color="#7fc0ff" stop-opacity="0"/>
    </linearGradient>
    <linearGradient id="reflection-fade" x1="0" x2="0" y1="0" y2="1">
      <stop offset="0" stop-color="#fff" stop-opacity="0.35"/>
      <stop offset="1" stop-color="#fff" stop-opacity="0"/>
    </linearGradient>
    <mask id="reflection-mask">
      <rect x="0" y="735" width="816" height="70" fill="url(#reflection-fade)"/>
    </mask>

    <text id="line-emergency" class="title-line" x="48" y="446" font-size="128" textLength="720" lengthAdjust="spacingAndGlyphs">EMERGENCY</text>
    <text id="line-critical" class="title-line" x="66" y="564" font-size="128" textLength="690" lengthAdjust="spacingAndGlyphs">&amp; CRITICAL</text>
    <text id="line-care" class="title-line" x="120" y="630" font-size="64" textLength="576" lengthAdjust="spacingAndGlyphs">CARE ULTRASOUND</text>
    <text id="line-course" class="title-line" x="198" y="732" font-size="128" textLength="438" lengthAdjust="spacingAndGlyphs">COURSE</text>

    <g id="title-block">
      <use href="#line-emergency"/>
      <use href="#line-critical"/>
      <use href="#line-care"/>
      <use href="#line-course"/>
    </g>
  </defs>

  <rect width="816" height="1200" fill="url(#bg-glow)"/>
  <rect width="816" height="600" fill="url(#top-sheen)"/>

  <text class="presenter" x="408" y="82" text-anchor="middle" font-size="27">YOUR <tspan class="company" font-size="34">COMPANY</tspan> PRESENTS</text>
  <text class="event-date" x="750" y="138" text-anchor="end" font-size="46" transform="skewX(-10) translate(22 0)">18-07-2014</text>

  <!-- title: 3D extrusion -->
  <g class="title-3d">
    <use href="#title-block" fill="var(--extrude-3)" transform="translate(7 8)"/>
    <use href="#title-block" fill="var(--extrude-3)" transform="translate(6 7)"/>
    <use href="#title-block" fill="var(--extrude-2)" transform="translate(5 6)"/>
    <use href="#title-block" fill="var(--extrude-2)" transform="translate(4 5)"/>
    <use href="#title-block" fill="var(--extrude-1)" transform="translate(3 3)"/>
    <use href="#title-block" fill="var(--extrude-1)" transform="translate(2 2)"/>
    <use href="#title-block" fill="var(--extrude-1)" transform="translate(1 1)"/>
    <use href="#title-block" fill="var(--white)"/>
  </g>

  <g class="title-reflection" mask="url(#reflection-mask)">
    <use href="#line-course" fill="var(--white)" transform="translate(0 1470) scale(1 -1)"/>
  </g>

  <g class="lens-flare">
    <ellipse cx="290" cy="510" rx="150" ry="60" fill="url(#flare)" opacity="0.8"/>
    <rect x="60" y="508" width="470" height="4" fill="url(#flare-streak)"/>
    <circle cx="290" cy="510" r="10" fill="#ffffff" opacity="0.9"/>
  </g>

  <g class="tagline" transform="skewX(-12)">
    <text x="592" y="877" text-anchor="middle" font-size="38">TEACH <tspan class="highlight" font-size="42">STUDENTS</tspan> ABOUT THE USE</text>
    <text x="604" y="937" text-anchor="middle" font-size="38">OF ULTRASOUND FOR VERY SICK PATIENTS</text>
  </g>

  <g class="contact" transform="skewX(-10)">
    <text x="600" y="1096" text-anchor="middle" font-size="29">VISIT OUR WEBSITE : WWW.WEBSITE.COM</text>
    <text x="606" y="1140" text-anchor="middle" font-size="29">YOUR ADRESSE HERE .4120 HARBOR RD. CASABLANCA,</text>
  </g>
</svg>
</body>
</html>
```